Electrical flyer

We would like a flyer designed advertising "Does your house need a re-wire?" Potential fire hazards exist in houses constructed pre 1970. You're electrical cabling has insulation that corrodes leaving bare cables in the ceiling space. To find out more google VIR cable. To find out if you need a re-wire contact us on 0493 527 804 for a free assessment. We would like it to be quite confronting and grab peoples attention.

Target Market(s)

40-80 year olds

Industry/Entity Type

Electrical

Requirements
Must have
• Shock and confrontation, attention grabbing

```html
<!DOCTYPE html>
<html lang="en">
<head>
<meta charset="utf-8">
<title>Does Your House Need a Re-Wire? – Velta Electrical</title>
<link rel="stylesheet" href="https://fonts.googleapis.com/css2?family=Montserrat:wght@700;800&family=Roboto+Condensed:wght@300;400;700&display=swap">
<style>
  :root {
    --sky-top: #e2f1f6;
    --sky-bottom: #cde6ef;
    --teal: #0b9a9b;
    --teal-deep: #0a8f8c;
    --grey-head: #7b7b7b;
    --rule: #8c8f92;
    --ink: #1f1f1f;
    --box-text: #eef6f6;
    --band: rgba(128, 138, 146, 0.62);
    --band-text: #4d5357;
  }
  * { margin: 0; padding: 0; box-sizing: border-box; }
  html, body { width: 927px; height: 1200px; overflow: hidden; }
  body { background: var(--sky-bottom); }
  .flyer {
    position: relative;
    width: 927px;
    height: 1200px;
    overflow: hidden;
    background: linear-gradient(180deg, var(--sky-top) 0%, #d8ecf3 40%, var(--sky-bottom) 100%);
    font-family: "Roboto Condensed", sans-serif;
  }
  .headline {
    position: absolute;
    top: 108px;
    left: 0;
    width: 100%;
    text-align: center;
    font-family: "Montserrat", sans-serif;
    line-height: 1;
  }
  .headline__lead {
    display: block;
    color: var(--teal);
    font-weight: 800;
    font-size: 72px;
    letter-spacing: -1px;
  }
  .headline__question {
    display: block;
    margin-top: 6px;
    color: var(--grey-head);
    font-weight: 700;
    font-size: 40px;
    letter-spacing: -0.5px;
  }
  .rule {
    position: absolute;
    left: 0;
    width: 100%;
    height: 2px;
    background: linear-gradient(90deg, rgba(140,143,146,0.35), var(--rule) 50%, rgba(140,143,146,0.35));
  }
  .rule--top { top: 251px; }
  .rule--bottom { top: 401px; }
  .intro {
    position: absolute;
    top: 284px;
    left: 0;
    width: 100%;
    text-align: center;
    color: var(--ink);
    font-weight: 400;
    font-size: 20px;
    line-height: 30px;
  }
  .cta-line {
    position: absolute;
    top: 509px;
    left: 0;
    width: 100%;
    height: 2px;
    background: var(--teal);
  }
  .cta {
    position: absolute;
    top: 441px;
    left: 54px;
    width: 818px;
    height: 142px;
    background: var(--teal);
    text-align: center;
    padding-top: 34px;
  }
  .cta__prompt {
    color: var(--box-text);
    font-weight: 300;
    font-size: 28px;
    line-height: 1;
  }
  .cta__action {
    margin-top: 8px;
    color: #0c0c0c;
    font-weight: 300;
    font-size: 42px;
    line-height: 1;
    letter-spacing: -0.5px;
  }
  .cta__phone { font-weight: 700; }
  .photo {
    position: absolute;
    top: 628px;
    left: 0;
    width: 927px;
    height: 572px;
    background:
      linear-gradient(180deg, rgba(205,230,239,0) 0%, rgba(205,230,239,0) 100%),
      linear-gradient(90deg, #a4562f 0%, #d9a385 22%, #efc9b2 38%, #cde6ef 50%, #e7b79b 62%, #c98c70 78%, #1c1c1c 100%);
    opacity: 0.9;
  }
  .brand-band {
    position: absolute;
    top: 1032px;
    left: 0;
    width: 100%;
    height: 142px;
    background: var(--band);
    text-align: center;
  }
  .brand-band__name {
    margin-top: 34px;
    color: var(--teal-deep);
    font-family: "Montserrat", sans-serif;
    font-weight: 700;
    font-size: 34px;
    letter-spacing: 1px;
    line-height: 1;
  }
  .brand-band__licence {
    margin-top: 14px;
    color: var(--band-text);
    font-size: 13px;
    letter-spacing: 6px;
    line-height: 1;
  }
</style>
</head>
<body>
  <main class="flyer">
    <h1 class="headline">
      <span class="headline__lead">DOES YOUR</span>
      <span class="headline__question">HOUSE NEED A RE-WIRE?</span>
    </h1>

    <div class="rule rule--top"></div>
    <p class="intro">
      Potential fire hazards exist in houses constructed pre 1970. You're electrical<br>
      cabling has insulation that corrodes leaving bare cables in the ceiling space.<br>
      To find out more google VIR cable.
    </p>
    <div class="rule rule--bottom"></div>

    <div class="cta-line"></div>
    <section class="cta">
      <p class="cta__prompt">TO FIND OUT IF YOU NEED A RE-WIRE CONTACT US ON</p>
      <p class="cta__action"><span class="cta__phone">0493 527 804</span> FOR A FREE ASSESSMENT.</p>
    </section>

    <div class="photo" role="img" aria-label="Photograph of a woman and a man in profile, face to face, shouting angrily at each other against a pale sky"></div>

    <footer class="brand-band">
      <p class="brand-band__name">VELTA ELECTRICAL</p>
      <p class="brand-band__licence">EC20587</p>
    </footer>
  </main>
</body>
</html>
```